Creative Brochure for Beauty School

We need a brochure designed on legal sized paper (8.5" X 14"), folded in half, and stapled in the middle, to create an 8-page (including covers) project. Therefore, your design for each page should be prepared in 7"x8.5" size (vertical). The brochure should have the look and feel of a magazine (a couple of samples attached to brief files for your reference). Think a magazine published for individuals interested in becoming beauty and wellness professionals. GET CREATIVE! We give you complete creative freedom.

NOTE: FOR DESIGN SELECTION PURPOSES, WE ONLY REQUIRE THE COVER AND 1-2 PAGES. I DO NOT NEED THE COMPLETED BROCHURE, AS I REALIZE TIME IS MONEY. WE WILL WORK TOGETHER TO COMPLETE PROJECT ONCE A DESIGN IS SELECTED.

Our school has been in business for over a decade and provides education in beauty and wellness programs. The purpose of this brochure is to showcase all our program offerings to prospect students in a creative and inspiring way. The brochure will be provided to everyone that inquires about our programs of study and it should provide basic and straightforward information about the school and each program, along with notable facts about us or the industry.

The design should consist of the following elements:

1. Front Cover page. Needs to be beautifully designed and eye catching, having the look and feel of a magazine cover. Cover must have:

- Logo: used as the "magazine’s" masthead
- Tag Line::::::: Beautify your future
-main image (use any of the attached images OR any stock image that can be purchased later by us). Only requirement is that the image has to be of stunning quality.
-Cover lines: (Designers, you may show your creativity). Some ideas on cover lines:
+8 beauty and wellness programs ::::: Endless career opportunities
+Academic Excellence: 82.44% graduation rate in 2012-2013^^
+Affordable tuition and financial assistance programs available.*
+ Miami’s premier choice for beauty education

-any other element desired to enhance the magazine theme.

-Required Disclaimer: (required disclaimers but can and should be very small print)

^^Based on TRELVIN’ 2012-13 Annual Report
*Financial aid available to those who qualify.

2. Must dedicate an area for each of our programs of study. We offer 8 programs, but some can be combined into one page in the layout. The programs can be divided into 2 main categories: beauty programs and spa/wellness programs. The content for each program will be provided later, depending on the design, but we do not expect it to exceed 3-4 sentences of main text for each program. The layout should be easy to read through use of typography, headlines, pull quotes, font colors and hierarchy. The copy should not be lengthy, rather concise and easy to read.

***The beauty programs are:
-Cosmetology (this is the main program so give it the importance it merits in the design)
-Makeup Artistry
-Barber (mainly designed for male students, if images are used, they should be male model)

***Spa/Wellness programs:
-Spa Therapy
-Massage Therapy (can showcase a photo of a male if needed to create diversity)
-Skin Care
-Manicure, Pedicure & Nail Extensions
-Full Specialist (combines the Skin Care and Manicure, Pedicure & Nail Extensions programs)

FYI: Please use the names of the programs verbatim.

3. Areas for (brief) industry content, testimonials (which can include a picture of the individual, to be provided later, should the design require it), facts about the school or industry, and any other idea you come up with.

4. Back cover. Allow area for mailing.

I have added several photos to this brief that you may use as you wish, although some may need Photoshopping. Please use any other photo you want, as long as you have copyrights or if we can buy the rights to the image later. Also added to files, photo of business card and screenshot of website design (no published yet) for color reference.

**This design will require 2 language versions, one in English and one in Spanish. Once a design is selected, we will provide all the necessary text in English and Spanish to allow you to complete.
Updates

Hello everyone:

I have added to the design brief a Microsoft word document with all the (English) text that we need to add to the brochure. I will really appreciate it if you go ahead and prepare a couple of these pages, to match the look and feel of the front cover, using the text and specifications provided in that document. I give you complete freedom in designing the body of the brochure. You may re-arrange the text, as long as you use everything or manage to convey the same message. If you feel that something in the text can be said differently, let me know, or present it. The text is not set in stone, we are open to your creative ideas.

Thanks-

Target Market(s)

Adults 18-49 years, typically our student body in comprised of 70% female / 30% male. The look should be modern, hip yet elegant and sophisticated.

Industry/Entity Type

Education

Requirements
Must have
• Magazine look and feel. Beautiful, eye catching design. We sell beauty, therefore design should be beautiful and glamorous, to go along with the industry.

-include tag line: Beautify your future
-Contact info:
Address: 5312 NW 4th Avenue. Miami, Fl 33052
Tel: 305-491-5836
Fax: 786-552-9274
www.marlowvista.edu
Instagram & Facebook icons / marlowvistabeautyschool
Should not have
• Should not have a corporate/serious feel or boring look.

```html
<!DOCTYPE html>
<html lang="en">
<head>
<meta charset="utf-8">
<title>Marlow Vista School of Beauty — Cover</title>
<link rel="stylesheet" href="https://fonts.googleapis.com/css2?family=Jost:wght@400;500&family=Archivo+Narrow:wght@700&family=Caprasimo&display=swap">
<style>
  :root {
    --stage: #eef1f5;
    --ink: #000000;
    --white: #ffffff;
    --lime: #6fd72a;
    --orange: #e8901f;
    --band: #f5a11a;
    --red: #e8231d;
    --yellow: #ffd21a;
    --blue: #3b7ce9;
    --cover-dark: #141414;
    --line-ink: #151515;
  }
  * { margin: 0; padding: 0; box-sizing: border-box; }
  html, body { width: 1200px; height: 1000px; overflow: hidden; }
  body { background: var(--stage); position: relative; }

  .cover {
    position: absolute; left: 230px; top: 50px;
    width: 740px; height: 900px;
    background: var(--ink); overflow: hidden;
  }
  .cover > * { position: absolute; white-space: nowrap; }

  .cover-photo {
    left: 280px; top: 0; width: 460px; height: 790px;
    background: radial-gradient(ellipse at 55% 45%, #8a5635 0%, #5a341f 35%, #2a1810 62%, var(--cover-dark) 85%);
  }

  .masthead {
    left: 40px; top: 88px;
    font-family: "Jost", sans-serif; font-weight: 500;
    font-size: 92px; line-height: 1; color: var(--white);
    letter-spacing: -1px;
  }
  .masthead-sub {
    left: 250px; top: 208px;
    font-family: "Jost", sans-serif; font-weight: 400;
    font-size: 30px; color: var(--white); letter-spacing: 0.5px;
  }

  .stat { left: 60px; top: 330px; font-family: "Archivo Narrow", sans-serif; font-weight: 700; }
  .stat-label {
    display: inline-block; background: var(--lime); color: var(--white);
    font-size: 20px; padding: 2px 10px;
  }
  .stat-figure {
    display: block; margin-left: 40px; width: 150px;
    color: var(--lime); font-size: 46px; line-height: 1.05;
    border-left: 4px solid var(--lime); border-top: 4px solid var(--lime);
    padding-left: 6px;
  }
  .stat-note { display: block; color: var(--lime); font-size: 20px; margin-top: 2px; }

  .tuition {
    left: 82px; top: 452px;
    font-family: "Jost", sans-serif; font-weight: 400;
    font-size: 28px; line-height: 1.18; color: var(--white);
  }
  .tuition .accent { color: var(--orange); }

  .photo-flower {
    left: 50px; top: 720px; width: 140px; height: 80px;
    background: radial-gradient(circle at 50% 50%, #f3f0c8 0%, #b9d98a 55%, #2b3a1a 100%);
  }

  .band {
    height: 40px;
    background: linear-gradient(90deg, var(--band) 0%, #f0a020 85%, rgba(245,161,26,0.35) 100%);
  }
  .band-wellness { left: 310px; top: 592px; width: 290px; }
  .band-beauty { left: 140px; top: 634px; width: 330px; }
  .band-programs { left: 250px; top: 674px; width: 310px; }
  .band-endless { left: 180px; top: 714px; width: 380px; }
  .band-opps { left: 190px; top: 754px; width: 330px; }

  .cover-line {
    font-family: "Caprasimo", serif; font-size: 32px; line-height: 40px;
    color: var(--line-ink);
  }
  .line-wellness { left: 324px; top: 592px; }
  .line-beauty { left: 150px; top: 634px; }
  .line-programs { left: 290px; top: 674px; }
  .line-endless { left: 196px; top: 714px; }
  .line-opps { left: 206px; top: 754px; }

  .amp {
    left: 232px; top: 548px;
    font-family: "Caprasimo", serif; font-size: 96px; line-height: 1;
    color: var(--line-ink); -webkit-text-stroke: 3px var(--yellow);
  }
  .count {
    left: 78px; top: 606px;
    font-family: "Caprasimo", serif; font-size: 140px; line-height: 1;
    color: var(--red); -webkit-text-stroke: 4px var(--yellow);
  }

  .photo-left {
    left: 90px; top: 800px; width: 140px; height: 80px;
    background: linear-gradient(160deg, #f3e9e2 0%, #c89a84 55%, #6b3f2e 100%);
    border: 3px solid var(--white);
  }
  .photo-right {
    left: 236px; top: 800px; width: 156px; height: 80px;
    background: linear-gradient(200deg, #fbf4ea 0%, #e8cdb6 50%, #b57a63 100%);
    border: 3px solid var(--white);
  }

  .stripe {
    left: 90px; top: 880px; width: 302px; height: 20px;
    background: repeating-linear-gradient(90deg, var(--lime) 0 12px, var(--ink) 12px 22px);
  }

  .tagline {
    left: 408px; top: 808px;
    font-family: "Caprasimo", serif; font-style: italic;
    font-size: 21px; line-height: 1.3; color: var(--blue);
    text-shadow: -2px -2px 0 var(--white), 2px -2px 0 var(--white), -2px 2px 0 var(--white), 2px 2px 0 var(--white);
  }
  .tagline .indent { display: block; padding-left: 10px; }
</style>
</head>
<body>
  <main class="cover">
    <div class="cover-photo" role="img" aria-label="Close-up portrait of a model with bright rainbow eye makeup and sleek dark hair"></div>

    <h1 class="masthead">Marlow Vista</h1>
    <p class="masthead-sub">SCHOOL OF BEAUTY</p>

    <div class="stat">
      <span class="stat-label">Academic Excellence</span>
      <span class="stat-figure">82.44%</span>
      <span class="stat-note">graduation rate in 2012-2013*</span>
    </div>

    <p class="tuition">Affordable tuition<br>and financial <span class="accent">assistance</span><br><span class="accent">programs available</span></p>

    <div class="photo-flower" role="img" aria-label="Soft pale flower detail"></div>

    <div class="band band-wellness"></div>
    <div class="band band-beauty"></div>
    <div class="band band-programs"></div>
    <div class="band band-endless"></div>
    <div class="band band-opps"></div>

    <span class="count">8</span>
    <span class="amp">&amp;</span>
    <span class="cover-line line-wellness">Wellness</span>
    <span class="cover-line line-beauty">Beauty</span>
    <span class="cover-line line-programs">programs</span>
    <span class="cover-line line-endless">Endless career</span>
    <span class="cover-line line-opps">opportunities</span>

    <div class="photo-left" role="img" aria-label="Model with dramatic green eye makeup"></div>
    <div class="photo-right" role="img" aria-label="Model with platinum curls and red lips"></div>
    <div class="stripe"></div>

    <p class="tagline">Miami's premier choice for<span class="indent">beauty education</span></p>
  </main>
</body>
</html>
```